Calvoterra business card

a nice business card with the logo,
Calvoterra
Teresa Lindqvist
Marketing Director
CH-1563 Geneva
Switzerland
+41 76 382 1904
email: Teresa.Lindqvist@calvoterra-mail.example

Target Market(s)

fertilizer business people, very nice and classic business card, normal size, make it nice and funky, try to make it different from the normal boring ones if possible.

Industry/Entity Type

Farming

Number of Pages Required

1 page

Requirements
Must have
• logo, Calvoterra, my name - mail and phone number
regular business card size for me to print easy please

```html
<!DOCTYPE html>
<html lang="en">
<head>
<meta charset="utf-8">
<title>Calvoterra — Teresa Lindqvist Business Card</title>
<link rel="stylesheet" href="https://fonts.googleapis.com/css2?family=Yellowtail&family=Arimo:wght@400;700&family=Crimson+Text:wght@700&display=swap">
<style>
  :root {
    --card-bg: #ffffff;
    --card-border: #a6a6a6;
    --band-bg: #c0c0c0;
    --band-text: #8c8c8c;
    --name-ink: #585858;
    --title-ink: #4a4a4a;
    --brand-ink: #8e8e8e;
    --brand-accent: #a3c93a;
  }
  * { margin: 0; padding: 0; box-sizing: border-box; }
  html, body {
    width: 1200px;
    height: 755px;
    overflow: hidden;
    background: var(--card-bg);
  }
  .card {
    position: relative;
    width: 1200px;
    height: 755px;
    background: var(--card-bg);
    border: 1px solid var(--card-border);
    overflow: hidden;
  }
  .brand {
    position: absolute;
    left: 67px;
    top: 272px;
    display: flex;
    align-items: center;
    gap: 12px;
  }
  .brand-dot {
    width: 16px;
    height: 16px;
    border-radius: 50%;
    background: var(--brand-accent);
  }
  .brand-name {
    font-family: "Arimo", Arial, sans-serif;
    font-weight: 700;
    font-size: 18px;
    letter-spacing: 5px;
    color: var(--brand-ink);
    text-transform: uppercase;
  }
  .holder {
    position: absolute;
    right: 36px;
    top: 14px;
    text-align: right;
  }
  .holder-name {
    font-family: "Yellowtail", cursive;
    font-size: 78px;
    line-height: 1.2;
    color: var(--name-ink);
    letter-spacing: 2px;
    white-space: nowrap;
  }
  .holder-role {
    margin-top: -8px;
    padding-right: 17px;
    font-family: "Arimo", Arial, sans-serif;
    font-size: 22px;
    color: var(--title-ink);
  }
  .contact-band {
    position: absolute;
    left: 0;
    right: 0;
    top: 528px;
    bottom: 0;
    background: var(--band-bg);
  }
  .contact-list {
    position: absolute;
    right: 36px;
    top: 8px;
    list-style: none;
    text-align: right;
    font-family: "Crimson Text", Georgia, serif;
    font-weight: 700;
    font-size: 34px;
    line-height: 54px;
    color: var(--band-text);
    white-space: nowrap;
  }
</style>
</head>
<body>
  <div class="card">
    <div class="brand">
      <span class="brand-dot"></span>
      <span class="brand-name">Calvoterra</span>
    </div>

    <header class="holder">
      <h1 class="holder-name">Teresa Lindqvist</h1>
      <p class="holder-role">Marketing Director</p>
    </header>

    <section class="contact-band">
      <ul class="contact-list">
        <li>CH-1563 Geneva</li>
        <li>Switzerland</li>
        <li>+41 76 382 1904</li>
        <li>email: Teresa.Lindqvist@calvoterra-mail.example</li>
      </ul>
    </section>
  </div>
</body>
</html>
```